VORN Paradigm. the way you communicate in every situation and in all environments.

I would like you to create a diagram depicting a very specific process of communication. it must follow the look of the diagram that i have attached. this is going to be used in a book called LANTERN. it is going to explain the fact that we communicate all the same way using this process as we communicate. it starts with the fact that everyone takes everything that is said personally and then moves on to filters, which is your own agenda or experience kicking in. then you move to your why it matters, which is your motivation and ends with the choice of words you use when you communicate. if you are going to be successful then you must separate the person from the issue.

Target Market(s)

market is executive business people around the world

Industry/Entity Type

Consulting

Font styles to use
Sans Serif

Colors

Designer to choose only greyscale colors for use in the design.

Requirements
Must have
• I would like it to have a diving/ocean/snorkel feel to it. The analogy we are using is to make a deep dive when you are communicating. it must have every part of the diagram you see, it starts at the top with the vorn paradigm (and the words) it then connects to the filters which connects to the why it matters with connects to the words and then end with the separating the person from the issue.
Nice to have
• we are writing a black and white book NO color. therefore the words should be clear and easy to read. Each section should be able to stand on its own so we can write about it separately.
Should not have
• the diagram DOES NOT have to look like the one i gave you. it must explain the fact that it starts with VORN and ends with Separate and must pass through the three areas to get to the SEPARATE.

```html
<!DOCTYPE html>
<html lang="en">
<head>
<meta charset="utf-8">
<title>VORN Paradigm – Communication Dive</title>
<link rel="stylesheet" href="https://fonts.googleapis.com/css2?family=Montserrat:wght@600;700&display=swap">
<style>
  :root {
    --sea-top: #e4e4e4;
    --sea-mid: #cfcfcf;
    --sea-deep: #8f8f8f;
    --flask-fill: #ffffff;
    --ink: #111111;
    --pipe-edge: #3a3a3a;
    --pipe-core: #ececec;
    --pipe-shine: #ffffff;
  }
  html, body {
    margin: 0;
    padding: 0;
    width: 920px;
    height: 1200px;
    overflow: hidden;
    background: var(--sea-top);
  }
  .diagram {
    display: block;
    width: 920px;
    height: 1200px;
  }
  .flask-outline { fill: var(--ink); stroke: var(--ink); stroke-width: 7; stroke-linejoin: round; }
  .flask-body { fill: var(--flask-fill); }
  .pipe-edge { fill: none; stroke: var(--pipe-edge); stroke-width: 31; }
  .pipe-core { fill: none; stroke: var(--pipe-core); stroke-width: 25; }
  .pipe-shine { fill: none; stroke: var(--pipe-shine); stroke-width: 5; opacity: .8; }
  .stage-label {
    font-family: "Montserrat", sans-serif;
    font-weight: 600;
    font-size: 14.5px;
    fill: var(--ink);
  }
  .stage-text {
    font-family: "Montserrat", sans-serif;
    font-weight: 700;
    font-size: 20.5px;
    fill: var(--ink);
    text-anchor: middle;
  }
  .stage-note {
    font-family: "Montserrat", sans-serif;
    font-weight: 600;
    font-size: 13px;
    fill: var(--ink);
    text-anchor: middle;
  }
</style>
</head>
<body>
<svg class="diagram" viewBox="0 0 920 1200" xmlns="http://www.w3.org/2000/svg">
  <defs>
    <linearGradient id="sea-gradient" x1="0" y1="0" x2="0" y2="1">
      <stop offset="0" stop-color="var(--sea-top)"/>
      <stop offset="0.7" stop-color="var(--sea-mid)"/>
      <stop offset="1" stop-color="var(--sea-deep)"/>
    </linearGradient>
    <path id="arc-paradigm" d="M393,82 Q463,62 533,82"/>
    <path id="arc-filters" d="M88,308 Q153,290 218,308"/>
    <path id="arc-matters" d="M390,539 Q460,521 530,539"/>
    <path id="arc-words" d="M707,781 Q767,763 827,781"/>
    <path id="arc-todo" d="M405,1023 Q460,1007 515,1023"/>
  </defs>

  <rect class="sea-scene" x="0" y="0" width="920" height="1200" fill="url(#sea-gradient)" role="img" aria-label="Underwater ocean scene with light ripples, swimming fish, rising bubbles and coral on the seabed"/>

  <!-- Flask outlines -->
  <g class="flask-outlines">
    <ellipse class="flask-outline" cx="463" cy="120" rx="126" ry="98"/>
    <rect class="flask-outline" x="282" y="92" width="80" height="56" rx="22"/>

    <ellipse class="flask-outline" cx="165" cy="368" rx="143" ry="98"/>
    <rect class="flask-outline" x="132" y="205" width="48" height="110" rx="20"/>
    <rect class="flask-outline" x="270" y="318" width="66" height="82" rx="24"/>

    <ellipse class="flask-outline" cx="478" cy="601" rx="148" ry="98"/>
    <rect class="flask-outline" x="440" y="442" width="47" height="110" rx="20"/>
    <rect class="flask-outline" x="590" y="560" width="52" height="78" rx="24"/>

    <ellipse class="flask-outline" cx="753" cy="842" rx="142" ry="96"/>
    <rect class="flask-outline" x="743" y="682" width="47" height="110" rx="20"/>
    <rect class="flask-outline" x="582" y="800" width="60" height="77" rx="24"/>

    <ellipse class="flask-outline" cx="460" cy="1082" rx="150" ry="100"/>
    <rect class="flask-outline" x="437" y="920" width="47" height="110" rx="20"/>
  </g>

  <!-- Flask fills -->
  <g class="flask-bodies">
    <ellipse class="flask-body" cx="463" cy="120" rx="126" ry="98"/>
    <rect class="flask-body" x="282" y="92" width="80" height="56" rx="22"/>

    <ellipse class="flask-body" cx="165" cy="368" rx="143" ry="98"/>
    <rect class="flask-body" x="132" y="205" width="48" height="110" rx="20"/>
    <rect class="flask-body" x="270" y="318" width="66" height="82" rx="24"/>

    <ellipse class="flask-body" cx="478" cy="601" rx="148" ry="98"/>
    <rect class="flask-body" x="440" y="442" width="47" height="110" rx="20"/>
    <rect class="flask-body" x="590" y="560" width="52" height="78" rx="24"/>

    <ellipse class="flask-body" cx="753" cy="842" rx="142" ry="96"/>
    <rect class="flask-body" x="743" y="682" width="47" height="110" rx="20"/>
    <rect class="flask-body" x="582" y="800" width="60" height="77" rx="24"/>

    <ellipse class="flask-body" cx="460" cy="1082" rx="150" ry="100"/>
    <rect class="flask-body" x="437" y="920" width="47" height="110" rx="20"/>
  </g>

  <!-- Connecting pipes -->
  <g class="pipes">
    <path class="pipe-edge" d="M300,120 H190 Q156,120 156,154 V222"/>
    <path class="pipe-core" d="M300,120 H190 Q156,120 156,154 V222"/>
    <path class="pipe-shine" d="M296,113 H190 Q149,113 149,154 V218"/>

    <path class="pipe-edge" d="M330,362 H430 Q463,362 463,396 V458"/>
    <path class="pipe-core" d="M330,362 H430 Q463,362 463,396 V458"/>
    <path class="pipe-shine" d="M334,355 H430 Q470,355 470,396 V454"/>

    <path class="pipe-edge" d="M632,598 H733 Q767,598 767,632 V698"/>
    <path class="pipe-core" d="M632,598 H733 Q767,598 767,632 V698"/>
    <path class="pipe-shine" d="M636,591 H733 Q774,591 774,632 V694"/>

    <path class="pipe-edge" d="M592,837 H494 Q460,837 460,871 V936"/>
    <path class="pipe-core" d="M592,837 H494 Q460,837 460,871 V936"/>
    <path class="pipe-shine" d="M588,830 H494 Q453,830 453,871 V932"/>
  </g>

  <!-- Stage 1 -->
  <g class="stage stage-paradigm">
    <text class="stage-label"><textPath href="#arc-paradigm" startOffset="50%" text-anchor="middle">VORN Paradigm</textPath></text>
    <text class="stage-text" x="463" y="119">When words are</text>
    <text class="stage-text" x="463" y="145">taken personally,</text>
    <text class="stage-text" x="463" y="171">what happens?</text>
  </g>

  <!-- Stage 2 -->
  <g class="stage stage-filters">
    <text class="stage-label"><textPath href="#arc-filters" startOffset="50%" text-anchor="middle">Your Filters</textPath></text>
    <text class="stage-text" x="153" y="346">An accumulation</text>
    <text class="stage-text" x="153" y="372">of your experience,</text>
    <text class="stage-text" x="153" y="398">knowledge and</text>
    <text class="stage-text" x="153" y="423">values.</text>
  </g>

  <!-- Stage 3 -->
  <g class="stage stage-matters">
    <text class="stage-label"><textPath href="#arc-matters" startOffset="50%" text-anchor="middle">Why it Matters</textPath></text>
    <text class="stage-text" x="460" y="580">This is your</text>
    <text class="stage-text" x="460" y="606">compass. It is what</text>
    <text class="stage-text" x="460" y="632">motivates you,</text>
    <text class="stage-text" x="460" y="657">what drives you.</text>
  </g>

  <!-- Stage 4 -->
  <g class="stage stage-words">
    <text class="stage-label"><textPath href="#arc-words" startOffset="50%" text-anchor="middle">Your Words</textPath></text>
    <text class="stage-text" x="767" y="820">This is your</text>
    <text class="stage-text" x="767" y="845">immediate response,</text>
    <text class="stage-text" x="767" y="871">verbal.</text>
    <text class="stage-note" x="767" y="890">or perhaps non-verbal</text>
  </g>

  <!-- Stage 5 -->
  <g class="stage stage-todo">
    <text class="stage-label"><textPath href="#arc-todo" startOffset="50%" text-anchor="middle">What To Do</textPath></text>
    <text class="stage-text" x="460" y="1064">Separate the</text>
    <text class="stage-text" x="460" y="1089">Person</text>
    <text class="stage-text" x="460" y="1115">from the</text>
    <text class="stage-text" x="460" y="1140">Issue</text>
  </g>
</svg>
</body>
</html>
```